Facebook, Twitter and Linkedin cover image design

Looking to update the facebook, twitter and aLinkedin cover images for Tandem Accounts . website www.tandacct.example
https://www.prolinknet.example/company/tandem-accounts-llc/mycompany/?viewAsMember=true
https://www.socialpage.example/tandacct
https://chirpline.example/tandacct

```html
<!DOCTYPE html>
<html lang="en">
<head>
<meta charset="utf-8">
<title>Tandem Accounts – Social Cover Images</title>
<link rel="stylesheet" href="https://fonts.googleapis.com/css2?family=Poppins:ital,wght@0,400;0,500;0,600;0,700;1,700&display=swap">
<style>
  :root {
    --stage: #474747;
    --label: #ffffff;
    --sky: #e0f1fc;
    --sky-deep: #cfe6f7;
    --ink: #2a2a2a;
    --orange: #f25c05;
    --green: #4c8b3f;
    --white: #ffffff;
    --illus-a: #a9c6f2;
    --illus-b: #7da3e8;
  }
  * { box-sizing: border-box; margin: 0; padding: 0; }
  html, body { width: 1200px; height: 1180px; overflow: hidden; }
  body {
    background: var(--stage);
    font-family: "Poppins", sans-serif;
    position: relative;
  }
  .platform-label {
    position: absolute; left: 0; width: 1200px; text-align: center;
    color: var(--label); font-size: 18px; font-weight: 500; line-height: 1;
  }
  .banner {
    position: absolute; overflow: hidden;
    background: linear-gradient(100deg, var(--sky) 0%, var(--sky) 45%, var(--sky-deep) 70%, var(--sky) 100%);
  }
  .banner > * { position: absolute; }
  .band { left: 0; right: 0; bottom: 0; background: var(--green); }
  .headline { color: var(--ink); font-weight: 700; line-height: 1; white-space: nowrap; }
  .headline .accent { color: var(--orange); display: block; }
  .headline .accent em { font-style: italic; }
  .tagline { color: var(--ink); font-weight: 500; white-space: nowrap; }
  .tab {
    background: var(--orange); color: var(--white); font-weight: 700;
    display: flex; align-items: center;
    clip-path: polygon(0 0, calc(100% - var(--notch)) 0, 100% 50%, calc(100% - var(--notch)) 100%, 0 100%);
  }
  .illustration {
    border-radius: 48% 52% 40% 44%;
    background: linear-gradient(135deg, var(--illus-a), var(--illus-b));
  }
  .brand { display: flex; align-items: center; color: var(--ink); font-weight: 600; line-height: 1.05; white-space: nowrap; text-transform: uppercase; }
  .brand .mark { background: var(--green); flex: none; }
  .industries { list-style: none; color: var(--white); font-weight: 500; white-space: nowrap; }
  .industries li { display: flex; align-items: center; }
  .industries svg { flex: none; }
  .call {
    background: var(--orange); color: var(--white); font-weight: 500;
    display: flex; align-items: center; white-space: nowrap;
    clip-path: polygon(var(--notch) 0, 100% 0, 100% 100%, var(--notch) 100%, 0 50%);
  }

  /* Facebook */
  .cover-fb { left: 350px; top: 141px; width: 500px; height: 190px; }
  .cover-fb .band { top: 109px; }
  .cover-fb .headline { left: 8px; top: 10px; font-size: 18.6px; }
  .cover-fb .headline .accent { margin-top: 3px; }
  .cover-fb .tagline { left: 9px; top: 54px; font-size: 11px; line-height: 15px; }
  .cover-fb .tab { left: 0; top: 96px; width: 147px; height: 27px; font-size: 12px; padding-left: 8px; --notch: 10px; }
  .cover-fb .illustration { left: 287px; top: 7px; width: 155px; height: 95px; }
  .cover-fb .brand { right: 12px; top: 6px; font-size: 6.5px; gap: 3px; }
  .cover-fb .brand .mark { width: 14px; height: 14px; }
  .cover-fb .industries { font-size: 9px; line-height: 17.5px; }
  .cover-fb .industries svg { width: 10px; height: 10px; margin-right: 4px; }
  .cover-fb .col-1 { left: 8px; top: 133px; }
  .cover-fb .col-2 { left: 213px; top: 133px; }
  .cover-fb .col-3 { left: 329px; top: 134px; line-height: 12px; font-size: 8.2px; }
  .cover-fb .col-3 li { align-items: flex-start; }
  .cover-fb .call { left: 322px; top: 163px; width: 178px; height: 19px; font-size: 13.5px; padding-left: 17px; --notch: 6px; }

  /* Twitter */
  .cover-tw { left: 143px; top: 428px; width: 914px; height: 305px; }
  .cover-tw .band { top: 166px; }
  .cover-tw .headline { left: 15px; top: 13px; font-size: 34px; }
  .cover-tw .headline .accent { margin-top: 5px; }
  .cover-tw .tagline { left: 16px; top: 88px; font-size: 18px; line-height: 23px; }
  .cover-tw .tab { left: 0; top: 143px; width: 270px; height: 51px; font-size: 25px; padding-left: 11px; --notch: 20px; }
  .cover-tw .illustration { left: 545px; top: 12px; width: 260px; height: 152px; }
  .cover-tw .brand { right: 31px; top: 11px; font-size: 10px; gap: 4px; }
  .cover-tw .brand .mark { width: 25px; height: 25px; }
  .cover-tw .industries { font-size: 17px; line-height: 32px; }
  .cover-tw .industries svg { width: 20px; height: 20px; margin-right: 8px; }
  .cover-tw .col-1 { left: 9px; top: 203px; }
  .cover-tw .col-2 { left: 392px; top: 202px; }
  .cover-tw .col-3 { left: 605px; top: 207px; line-height: 22px; font-size: 15.5px; }
  .cover-tw .col-3 svg { margin-right: 5px; }
  .cover-tw .col-3 li { align-items: flex-start; }
  .cover-tw .call { left: 593px; top: 257px; width: 321px; height: 39px; font-size: 25px; padding-left: 31px; --notch: 11px; }

  /* LinkedIn */
  .cover-li { left: 113px; top: 825px; width: 971px; height: 241px; }
  .cover-li .band { top: 139px; }
  .cover-li .headline { left: 247px; top: 13px; font-size: 31px; }
  .cover-li .headline .accent { margin-top: 2px; }
  .cover-li .tagline { left: 249px; top: 77px; font-size: 17px; line-height: 21px; }
  .cover-li .tab { left: 247px; top: 126px; width: 150px; height: 27px; font-size: 13.5px; padding-left: 12px; --notch: 9px; }
  .cover-li .illustration { left: 659px; top: 5px; width: 220px; height: 128px; }
  .cover-li .brand { right: 10px; top: 14px; font-size: 8.5px; gap: 3px; }
  .cover-li .brand .mark { width: 22px; height: 22px; }
  .cover-li .industries { font-size: 12.4px; line-height: 20.5px; }
  .cover-li .industries svg { width: 11px; height: 11px; margin-right: 4px; }
  .cover-li .col-1 { left: 248px; top: 161px; }
  .cover-li .col-2 { left: 544px; top: 161px; }
  .cover-li .col-3 { left: 737px; top: 164px; line-height: 14px; font-size: 11px; }
  .cover-li .col-3 li { align-items: flex-start; }
  .cover-li .call { left: 745px; top: 201px; width: 226px; height: 25px; font-size: 13.5px; padding-left: 17px; --notch: 6px; }
</style>
</head>
<body>
<svg width="0" height="0" style="position:absolute">
  <symbol id="tick" viewBox="0 0 24 24">
    <rect x="2" y="4" width="17" height="17" rx="3" fill="none" stroke="#fff" stroke-width="2.4"/>
    <path d="M6 12l4 4 11-12" fill="none" stroke="#fff" stroke-width="3" stroke-linecap="round" stroke-linejoin="round"/>
  </symbol>
</svg>

<p class="platform-label" style="top:98px">Facebook</p>
<section class="banner cover-fb">
  <div class="band"></div>
  <h1 class="headline">INCREASE CASH FLOW,<span class="accent"><em>GROW</em> YOUR BUSINESS!</span></h1>
  <p class="tagline">Tired Of Banking Your Customers?<br>Get Fast Invoice Payments!</p>
  <div class="illustration" role="img" aria-label="Illustration of a large invoice on a monitor with people, a calculator and gold coins"></div>
  <div class="brand"><span class="mark"></span><span>Tandem<br>Accounts</span></div>
  <h2 class="tab">INDUSTRIES SERVED</h2>
  <ul class="industries col-1">
    <li><svg><use href="#tick"/></svg>Automotive/Truck Dealerships</li>
    <li><svg><use href="#tick"/></svg>Repair Shops &amp; Parts Distributors</li>
    <li><svg><use href="#tick"/></svg>Industrial Maintenance Transportation</li>
  </ul>
  <ul class="industries col-2">
    <li><svg><use href="#tick"/></svg>Staffing</li>
    <li><svg><use href="#tick"/></svg>Transportation</li>
    <li><svg><use href="#tick"/></svg>Oil &amp; Gas</li>
  </ul>
  <ul class="industries col-3">
    <li><svg><use href="#tick"/></svg><span>Storm Response, Utility Restoration<br>and Maintenance Services</span></li>
  </ul>
  <p class="call">Call us:&nbsp; 555.201.4477</p>
</section>

<p class="platform-label" style="top:394px">Twitter</p>
<section class="banner cover-tw">
  <div class="band"></div>
  <h1 class="headline">INCREASE CASH FLOW,<span class="accent"><em>GROW</em> YOUR BUSINESS!</span></h1>
  <p class="tagline">Tired Of Banking Your Customers?<br>Get Fast Invoice Payments!</p>
  <div class="illustration" role="img" aria-label="Illustration of a large invoice on a monitor with people, a calculator and gold coins"></div>
  <div class="brand"><span class="mark"></span><span>Tandem<br>Accounts</span></div>
  <h2 class="tab">INDUSTRIES SERVED</h2>
  <ul class="industries col-1">
    <li><svg><use href="#tick"/></svg>Automotive/Truck Dealerships</li>
    <li><svg><use href="#tick"/></svg>Repair Shops &amp; Parts Distributors</li>
    <li><svg><use href="#tick"/></svg>Industrial Maintenance Transportation</li>
  </ul>
  <ul class="industries col-2">
    <li><svg><use href="#tick"/></svg>Staffing</li>
    <li><svg><use href="#tick"/></svg>Transportation</li>
    <li><svg><use href="#tick"/></svg>Oil &amp; Gas</li>
  </ul>
  <ul class="industries col-3">
    <li><svg><use href="#tick"/></svg><span>Storm Response, Utility Restoration<br>and Maintenance Services</span></li>
  </ul>
  <p class="call">Call us:&nbsp; 555.201.4477</p>
</section>

<p class="platform-label" style="top:783px">linkedin</p>
<section class="banner cover-li">
  <div class="band"></div>
  <h1 class="headline">INCREASE CASH FLOW,<span class="accent"><em>GROW</em> YOUR BUSINESS!</span></h1>
  <p class="tagline">Tired Of Banking Your Customers?<br>Get Fast Invoice Payments!</p>
  <div class="illustration" role="img" aria-label="Illustration of a large invoice on a monitor with people, a calculator and gold coins"></div>
  <div class="brand"><span class="mark"></span><span>Tandem<br>Accounts</span></div>
  <h2 class="tab">INDUSTRIES SERVED</h2>
  <ul class="industries col-1">
    <li><svg><use href="#tick"/></svg>Automotive/Truck Dealerships</li>
    <li><svg><use href="#tick"/></svg>Repair Shops &amp; Parts Distributors</li>
    <li><svg><use href="#tick"/></svg>Industrial Maintenance Transportation</li>
  </ul>
  <ul class="industries col-2">
    <li><svg><use href="#tick"/></svg>Staffing</li>
    <li><svg><use href="#tick"/></svg>Transportation</li>
    <li><svg><use href="#tick"/></svg>Oil &amp; Gas</li>
  </ul>
  <ul class="industries col-3">
    <li><svg><use href="#tick"/></svg><span>Storm Response, Utility Restoration<br>and Maintenance Services</span></li>
  </ul>
  <p class="call">Call us:&nbsp; 555.201.4477</p>
</section>
</body>
</html>
```